New Business Card Design Project

Want a simple but attention grabbing business card. Back Side having mainly our logo and basic info-the front side a typical business card.

Contact Information for Business Card

Hearth & Tile Interiors
218 NW Larkspur Rd. Suite 207
Ankeny, Iowa 50021

phone- 515.482.7093

website is -htidesigns.com

```html
<!DOCTYPE html>
<html lang="en">
<head>
<meta charset="utf-8">
<title>Hearth &amp; Tile Interiors — Business Card</title>
<link rel="stylesheet" href="https://fonts.googleapis.com/css2?family=Montserrat:wght@400;500;600&display=swap">
<style>
  :root {
    --backdrop: #1b1d21;
    --card-navy: #0b1527;
    --accent-orange: #f0622a;
    --accent-blue: #2f80d4;
    --mark-blue: #3c6f9f;
    --text-white: #f2f4f8;
  }
  * { box-sizing: border-box; margin: 0; padding: 0; }
  html, body {
    width: 1200px; height: 900px; overflow: hidden;
    background: var(--backdrop);
    font-family: "Montserrat", sans-serif;
  }
  .sheet {
    width: 1200px; height: 900px;
    display: flex; flex-direction: column;
    align-items: center; justify-content: center; gap: 60px;
  }
  .card {
    width: 560px; height: 320px;
    background: var(--card-navy);
    position: relative;
    box-shadow: 0 12px 30px rgba(0,0,0,.5);
  }
  /* Front */
  .card-front .holder { position: absolute; left: 40px; top: 44px; }
  .holder-name {
    color: var(--accent-orange); font-weight: 600;
    font-size: 22px; letter-spacing: 1px; text-transform: uppercase;
  }
  .holder-title { color: var(--text-white); font-size: 14px; margin-top: 4px; }
  .card-front .details {
    position: absolute; right: 40px; bottom: 36px; width: 290px;
  }
  .company-name {
    color: var(--accent-orange); font-weight: 600; font-size: 20px;
    text-transform: uppercase; letter-spacing: .5px;
    display: flex; align-items: center; gap: 8px;
  }
  .company-name .dot {
    width: 10px; height: 10px; background: var(--accent-blue); flex: none;
  }
  .address {
    color: var(--text-white); font-size: 13px; line-height: 1.45;
    margin: 16px 0 14px;
  }
  .contact-list { list-style: none; color: var(--text-white); font-size: 13px; line-height: 1.6; }
  .contact-list li { display: flex; align-items: center; gap: 8px; }
  .contact-list svg { width: 12px; height: 12px; flex: none; }
  /* Back */
  .card-back { display: flex; align-items: center; justify-content: center; }
  .back-name {
    color: var(--mark-blue); font-weight: 600; font-size: 34px;
    text-transform: uppercase; letter-spacing: 2px; text-align: center;
  }
</style>
</head>
<body>
<main class="sheet">
  <section class="card card-front" aria-label="Business card front">
    <div class="holder">
      <p class="holder-name">Owen Calloway</p>
      <p class="holder-title">President</p>
    </div>
    <div class="details">
      <p class="company-name"><span class="dot"></span>Hearth &amp; Tile Interiors</p>
      <p class="address">218 NW Larkspur Rd. Suite 207<br>Ankeny, Iowa 50021</p>
      <ul class="contact-list">
        <li>
          <svg viewBox="0 0 12 12" aria-hidden="true"><path fill="var(--accent-blue)" d="M2.5 1l2 2.3-1 1.2c.7 1.5 1.8 2.6 3.3 3.3l1.2-1 2.3 2-1.2 1.7C5 10.5 1.5 7 .8 2.2z"/></svg>
          515.482.7093
        </li>
        <li>
          <svg viewBox="0 0 12 12" aria-hidden="true"><rect x="0.5" y="2" width="11" height="8" fill="var(--accent-blue)"/><path d="M1 2.5l5 4 5-4" stroke="var(--card-navy)" stroke-width="1" fill="none"/></svg>
          hello@htidesigns.com
        </li>
        <li>
          <svg viewBox="0 0 12 12" aria-hidden="true"><circle cx="6" cy="6" r="5.2" fill="none" stroke="var(--accent-blue)" stroke-width="1.3"/><path d="M.8 6h10.4M6 .8c-2.6 3-2.6 7.4 0 10.4M6 .8c2.6 3 2.6 7.4 0 10.4" stroke="var(--accent-blue)" stroke-width="1" fill="none"/></svg>
          www.htidesigns.com
        </li>
      </ul>
    </div>
  </section>

  <section class="card card-back" aria-label="Business card back">
    <p class="back-name">Hearth &amp; Tile Interiors</p>
  </section>
</main>
</body>
</html>
```